The Orchard of Virtue Customized for my Business

Hi! I am interested in getting some design ideas to take this Orchard of Virtue and put a bit of branding of my business into it. Open to any and all designs, this is intended to put on a 20"x24" or 16"x20" canvas so I can have it in my office for team training purposes. I have included a picture of the wall this canvas will go on. Thank you!

```html
<!DOCTYPE html>
<html lang="en">
<head>
<meta charset="utf-8">
<title>The Orchard of Virtue</title>
<link href="https://fonts.googleapis.com/css2?family=Rubik:wght@400;500;700;800&family=Lato:wght@400;700;900&display=swap" rel="stylesheet">
<style>
  :root {
    --ink: #231f20;
    --slate: #3f4042;
    --sky: #29abe2;
    --paper: #ffffff;
    --rim: #d6d6d6;
  }
  * { box-sizing: border-box; margin: 0; padding: 0; }
  html, body { width: 1000px; height: 1200px; overflow: hidden; background: var(--paper); }
  .stage {
    position: relative; width: 1750px; height: 2100px;
    transform: scale(0.5714286); transform-origin: 0 0;
    font-family: "Lato", sans-serif; color: var(--ink);
  }
  .frame { position: absolute; left: 0; top: 0; }

  .brand {
    position: absolute; left: 90px; top: 200px;
    display: flex; align-items: center; gap: 18px;
  }
  .brand-mark { width: 26px; height: 26px; background: var(--sky); }
  .brand-name {
    font-family: "Lato", sans-serif; font-weight: 700; font-size: 44px;
    color: var(--sky); letter-spacing: 6px; text-transform: uppercase;
  }

  .virtue { position: absolute; width: 320px; text-align: center; }
  .virtue-icon {
    display: block; width: 58px; height: 58px; margin: 0 auto 4px;
    border-radius: 14px; background: linear-gradient(135deg, var(--ink) 0%, var(--ink) 55%, var(--sky) 100%);
  }
  .virtue-name { font-family: "Rubik", sans-serif; font-weight: 700; font-size: 30px; line-height: 1.05; }
  .virtue-note { font-size: 19px; line-height: 1.25; }

  .block {
    position: absolute; width: 232px; height: 164px;
    border-radius: 50%; background: var(--ink);
    border: 2px solid var(--rim); overflow: hidden; color: var(--paper);
  }
  .block-title {
    height: 66px; background: var(--sky); color: var(--ink);
    font-family: "Rubik", sans-serif; font-weight: 500; font-size: 19px;
    display: flex; align-items: flex-end; justify-content: center;
    text-align: center; line-height: 1.05; padding-bottom: 8px;
  }
  .block-text {
    font-size: 12.5px; line-height: 1.2; text-align: center;
    padding: 9px 22px 0; font-weight: 700;
  }

  .title {
    position: absolute; left: 300px; top: 1503px; width: 1150px;
    text-align: center; font-family: "Lato", sans-serif; font-weight: 900;
    font-size: 86px; color: var(--ink); letter-spacing: -1px; line-height: 1;
  }
  .seal-name {
    position: absolute; left: 1463px; top: 1478px; width: 140px; height: 140px;
    display: flex; align-items: center; justify-content: center; text-align: center;
    font-family: "Lato", sans-serif; font-weight: 700; font-size: 17px; letter-spacing: 2px;
    color: var(--sky); line-height: 1.2;
  }
  .site {
    position: absolute; left: 490px; top: 1982px; width: 770px; height: 78px;
    border-radius: 39px; background: var(--sky); color: var(--paper);
    font-size: 38px; display: flex; align-items: center; justify-content: center;
  }
</style>
</head>
<body>
<div class="stage">
  <svg class="frame" width="1750" height="2100" viewBox="0 0 1750 2100" aria-hidden="true">
    <g fill="none" stroke="#231f20" stroke-width="3">
      <polyline points="543,545 770,545 875,395 980,545 1207,545"/>
      <polyline points="420,722 648,722 760,560"/>
      <polyline points="297,900 525,900 637,740"/>
      <polyline points="172,1082 400,1082 512,920"/>
      <polyline points="47,1262 275,1262 387,1100"/>
      <polyline points="1330,722 1102,722 990,560"/>
      <polyline points="1452,900 1225,900 1113,740"/>
      <polyline points="1578,1082 1350,1082 1238,920"/>
      <polyline points="1703,1262 1475,1262 1363,1100"/>
    </g>
    <path d="M858,460 Q875,436 892,460 L1612,1500 L138,1500 Z" fill="#3f4042"/>
    <rect x="125" y="1465" width="1500" height="175" rx="87" fill="#3f4042"/>
    <rect x="140" y="1478" width="1470" height="150" rx="75" fill="#29abe2"/>
    <circle cx="217" cy="1548" r="72" fill="#231f20" stroke="#ffffff" stroke-width="3"/>
    <circle cx="1533" cy="1548" r="72" fill="#231f20" stroke="#ffffff" stroke-width="3"/>
  </svg>
  <div role="img" aria-label="Handshake with a check mark icon" style="position:absolute;left:170px;top:1501px;width:94px;height:94px;border-radius:50%;background:linear-gradient(135deg,#29abe2,#ffffff);"></div>

  <div class="brand">
    <span class="brand-mark"></span>
    <span class="brand-name">Alder Creek</span>
  </div>

  <div class="virtue" style="left:523px;top:415px"><span class="virtue-icon" role="img" aria-label="Praying hands icon"></span><div class="virtue-name">Faith</div><div class="virtue-note">(through prayer)</div></div>
  <div class="virtue" style="left:922px;top:415px"><span class="virtue-icon" role="img" aria-label="Two people with scales icon"></span><div class="virtue-name">Patience</div><div class="virtue-note">(good things take time)</div></div>
  <div class="virtue" style="left:391px;top:598px"><span class="virtue-icon" role="img" aria-label="Person with raised arms icon"></span><div class="virtue-name">Fight</div><div class="virtue-note">(determined effort)</div></div>
  <div class="virtue" style="left:1032px;top:598px"><span class="virtue-icon" role="img" aria-label="Person with shield icon"></span><div class="virtue-name">Integrity</div><div class="virtue-note">(purity of intention)</div></div>
  <div class="virtue" style="left:261px;top:775px"><span class="virtue-icon" role="img" aria-label="Shield with person icon"></span><div class="virtue-name">Resourcefulness</div><div class="virtue-note">(proper judgement)</div></div>
  <div class="virtue" style="left:1157px;top:775px"><span class="virtue-icon" role="img" aria-label="Shield and thumbs up icon"></span><div class="virtue-name">Reliability</div><div class="virtue-note">(creates respect)</div></div>
  <div class="virtue" style="left:140px;top:958px"><span class="virtue-icon" role="img" aria-label="People exchanging icon"></span><div class="virtue-name">Adaptability</div><div class="virtue-note">(to any situation)</div></div>
  <div class="virtue" style="left:1288px;top:958px"><span class="virtue-icon" role="img" aria-label="Heart with hand icon"></span><div class="virtue-name">Honesty</div><div class="virtue-note">(in thought and action)</div></div>
  <div class="virtue" style="left:16px;top:1140px"><span class="virtue-icon" role="img" aria-label="Hands holding a globe icon"></span><div class="virtue-name">Ambition</div><div class="virtue-note">(for noble goals)</div></div>
  <div class="virtue" style="left:1401px;top:1140px"><span class="virtue-icon" role="img" aria-label="Raised hand with heart icon"></span><div class="virtue-name">Sincerity</div><div class="virtue-note">(Keeps friends)</div></div>

  <div class="block" style="left:759px;top:560px"><div class="block-title">COMPETITIVE<br>GREATNESS</div><div class="block-text">Be at our best when your best is needed. Enjoyment of a difficult challenge.</div></div>

  <div class="block" style="left:640px;top:740px"><div class="block-title">POISE</div><div class="block-text">Just being yourself. Being at ease in any situation. Never fighting yourself.</div></div>
  <div class="block" style="left:879px;top:740px"><div class="block-title">CONFIDENCE</div><div class="block-text">Respect without fear. May come from being prepared &amp; keeping all things in proper perspective.</div></div>

  <div class="block" style="left:520px;top:920px"><div class="block-title">CONDITION</div><div class="block-text">Mental-Moral-Physical. Rest, exercise &amp; diet must be considered. Moderation must be practiced. Dissipation must be eliminated.</div></div>
  <div class="block" style="left:759px;top:920px"><div class="block-title">SKILL</div><div class="block-text">Knowledge of &amp; the ability to properly &amp; quickly execute the fundamentals.</div></div>
  <div class="block" style="left:998px;top:920px"><div class="block-title">TEAM SPIRIT</div><div class="block-text">A genuine consideration for others. An eagerness to sacrifice personal interests of glory for the welfare of all.</div></div>

  <div class="block" style="left:400px;top:1100px"><div class="block-title">SELF-CONTROL</div><div class="block-text">Practice self-discipline &amp; keep emotions under control. Good judgement &amp; common sense are essential.</div></div>
  <div class="block" style="left:640px;top:1100px"><div class="block-title">ALERTNESS</div><div class="block-text">Be observing constantly. Stay open-minded. Be egar to learn &amp; improve.</div></div>
  <div class="block" style="left:879px;top:1100px"><div class="block-title">INITATIVE</div><div class="block-text">Cultivate the ability to make decisions &amp; think alone. Do not be afraid of failure but, learn from it.</div></div>
  <div class="block" style="left:1118px;top:1100px"><div class="block-title">INTENTNESS</div><div class="block-text">Set a realistic goal. Concentrate on its achievement by resisting all temptations &amp; being determined &amp; persistant.</div></div>

  <div class="block" style="left:281px;top:1280px"><div class="block-title">INDUSTRIOUSNESS</div><div class="block-text">There is no substitue for work. Worthwhile results come from hard work &amp; careful planning</div></div>
  <div class="block" style="left:520px;top:1280px"><div class="block-title">FRIENDSHIP</div><div class="block-text">Comes from mutual esteem, respect &amp; devotion. Like marriage it must not be taken for granted but requires a joint effort</div></div>
  <div class="block" style="left:759px;top:1280px"><div class="block-title">LOYALTY</div><div class="block-text">To yourself &amp; to all those depending upon you. Keep your self-respect.</div></div>
  <div class="block" style="left:998px;top:1280px"><div class="block-title">COOPERATION</div><div class="block-text">With all levels of your co-workers. Listen if you want to be heard. Be interested in finding the best way, not in having your own way.</div></div>
  <div class="block" style="left:1237px;top:1280px"><div class="block-title">ENTHUSIASM</div><div class="block-text">Brushes off upon those with whom you come in contact. You must truly enjoy what you are doing.</div></div>

  <div class="title">THE ORCHARD OF VIRTUE</div>
  <div class="seal-name">ALDER<br>CREEK</div>

  <div class="site">www.aldercreekwellness.com</div>
</div>
</body>
</html>
```